Beer Can Label named: ZAP Ginger Beer

We need a funky design for a Ginger Beer that is made from all natural ingredients. The label needs to be full of Colour, emphasis on the Ginger Root. ZAP (Zested And Poured)

Target Market(s)

None beer drinkers'

Requirements
Must have
• Name on the label must beer easy to read. Needs to be very colourful, playful & even a bit cheaky.
Nice to have
• A label that looks at the benefits of Ginger for the body in a fun artistic design.
Should not have
• Should NOT be a simple, basic, minimalistic design

```html
<!DOCTYPE html>
<html lang="en">
<head>
<meta charset="utf-8">
<title>ZAP Ginger Beer – Can Label</title>
<link href="https://fonts.googleapis.com/css2?family=Anton&family=Roboto+Condensed:wght@300;400&display=swap" rel="stylesheet">
<style>
  :root {
    --page-bg: #f0b13c;
    --label-pale: #fdfbe0;
    --label-yellow: #f2ec62;
    --swoosh-yellow: #f6d64a;
    --swoosh-orange: #ee8a2a;
    --band-purple: #9b2aa0;
    --brand-green: #2c7d46;
    --ginger-olive: #9a7a2c;
    --beer-purple: #8e2392;
    --tag-red: #e4202a;
    --bubble-line: #e2573a;
    --bubble-text: #5a4a3a;
    --root-tone: #e6cf9a;
    --leaf-green: #4d9a36;
  }
  * { margin: 0; padding: 0; box-sizing: border-box; }
  html, body { width: 800px; height: 1200px; overflow: hidden; }
  body { background: var(--page-bg); position: relative; }

  .label {
    position: absolute; left: 80px; top: 190px;
    width: 640px; height: 820px; overflow: hidden;
    background: radial-gradient(ellipse 60% 45% at 40% 10%, #ffffff 0%, var(--label-pale) 35%, var(--label-yellow) 100%);
  }
  .label-bands { position: absolute; inset: 0; }

  .brand-name {
    position: absolute; left: 82px; top: 516px;
    transform-origin: 0 0; transform: rotate(-90deg);
    font-family: "Anton", sans-serif; font-size: 250px; line-height: 205px;
    color: var(--brand-green); letter-spacing: 2px;
  }
  .brand-tag {
    position: absolute; left: 85px; top: 524px;
    background: var(--tag-red); color: #fff;
    font-family: "Anton", sans-serif; font-size: 19px; line-height: 29px;
    padding: 0 6px; letter-spacing: .3px;
  }
  .product-name {
    position: absolute; left: 304px; top: 150px;
    font-family: "Anton", sans-serif; line-height: 1;
  }
  .product-name .ginger { display: block; color: var(--ginger-olive); font-size: 92px; }
  .product-name .beer { display: block; color: var(--beer-purple); font-size: 128px; margin-top: -6px; }

  .ginger-root {
    position: absolute; left: 287px; top: 377px; width: 258px; height: 191px;
    background: radial-gradient(ellipse at 50% 50%, var(--root-tone) 0%, rgba(230,207,154,.6) 55%, rgba(230,207,154,0) 75%);
  }
  .leaf-sprig {
    position: absolute; left: 99px; top: 592px; width: 117px; height: 150px;
    background: radial-gradient(ellipse at 50% 50%, var(--leaf-green) 0%, rgba(77,154,54,.7) 45%, rgba(77,154,54,0) 72%);
  }

  .benefits { position: absolute; inset: 0; pointer-events: none; }
  .benefit {
    position: absolute; display: flex; align-items: center; justify-content: center;
    text-align: center; border: 2px solid var(--bubble-line); border-radius: 50%;
    font-family: "Roboto Condensed", sans-serif; font-weight: 300;
    color: var(--bubble-text); line-height: 1.15;
  }
  .benefit--digestion { left: 526px; top: 362px; width: 124px; height: 118px; font-size: 12.5px; padding: 0 18px 0 8px; }
  .benefit--pain { left: 540px; top: 505px; width: 112px; height: 98px; font-size: 12.5px; padding: 0 16px 0 4px; }
  .benefit--cancer { left: 211px; top: 576px; width: 181px; height: 78px; font-size: 17px; }
  .benefit--heart { left: 328px; top: 657px; width: 187px; height: 92px; font-size: 17px; }
</style>
</head>
<body>
  <main class="label">
    <svg class="label-bands" width="640" height="820" viewBox="0 0 640 820" aria-hidden="true">
      <path d="M0 660 C 200 610, 420 470, 640 330 L640 820 L0 820 Z" fill="var(--swoosh-yellow)"/>
      <path d="M0 690 C 220 660, 430 540, 640 420 L640 820 L0 820 Z" fill="var(--swoosh-orange)"/>
      <rect x="0" y="754" width="640" height="66" fill="var(--band-purple)"/>
    </svg>

    <div class="brand-name">ZAP</div>
    <div class="brand-tag">Zested And Poured</div>

    <h1 class="product-name">
      <span class="ginger">Ginger</span>
      <span class="beer">Beer</span>
    </h1>

    <div class="ginger-root" role="img" aria-label="Hand-drawn sketch of a ginger root with sliced pieces"></div>
    <div class="leaf-sprig" role="img" aria-label="Green serrated leaf sprig"></div>

    <div class="benefits">
      <p class="benefit benefit--digestion">Reducing gas and improving digestion Easing a cold or the flu</p>
      <p class="benefit benefit--pain">Relieving pain Reducing inflammation</p>
      <p class="benefit benefit--cancer">Lowering cancer risk</p>
      <p class="benefit benefit--heart">Supporting<br>cardiovascular health</p>
    </div>
  </main>
</body>
</html>
```